Geschäftspapiere für unternehmerische Holding für Beteiligungen, Projektgesellschaften und kaufmännische Steuerung
Zielgruppe
Die Hollwen GmbH ist eine unternehmerische Holding für Beteiligungen, Projektgesellschaften und kaufmännische Steuerung. Sie übernimmt Management-, Controlling- und Strukturierungsaufgaben für verbundene Unternehmen.
Zielgruppe sind Banken, Investoren, Geschäftspartner, Steuerberater, Rechtsanwälte, Behörden sowie Geschäftsführungen und Gesellschafter von Beteiligungs- und Projektgesellschaften.
Aufgabenstellung
Gesucht wird ein digitales Briefpapier für die Hollwen GmbH, das sowohl als PDF/Dokumentvorlage als auch beim Ausdruck professionell funktioniert.
Wichtig ist ein sehr klarer, hochwertiger und seriöser Auftritt. Das Design soll reduziert, strukturiert und geschäftlich wirken – keine verspielten Elemente, keine überladenen Grafiken, keine auffälligen Muster.
Das Briefpapier muss drucktauglich sein. Bitte ausreichende Druckränder und Sicherheitsabstände berücksichtigen, damit Kopf- und Fußbereich auch auf normalen Büro- und Laserdruckern sauber ausgegeben werden können. Das Layout soll sowohl digital als auch gedruckt stimmig aussehen.
Format: DIN A4 Hochformat.
Gewünschte Inhalte:
* Logo der Hollwen GmbH
* Firmenname: Hollwen GmbH
* Geschäftsanschrift: Lindauer Weg 52, 80339 München
* Telefon: 089 58210946
* E-Mail: info@hollwenbeta.example
* Webseite: hollwenbeta.example
* Geschäftsführung: Dipl.-Wirtschaftsing. (FH) Till Osterwald
* Registergericht / Amtsgericht München HRB 527081
* Bankverbindung IBAN DE918204 5571 0009 1826 40
Besonderer Wert liegt auf:
* hochwertiger Holding-/Investment-Anmutung
* sehr guter Lesbarkeit
* klarer Kopf- und Fußzeile
* sauberer Typografie
* professioneller Nutzbarkeit für Angebote, Verträge, Behörden- und Bankkorrespondenz
Bitte das Design so anlegen, dass es später als editierbare Word-/PDF-Vorlage genutzt werden kann und sowohl das Logo, als auch die Farben entsprechend verwenden.

```html
<!DOCTYPE html>
<html lang="de">
<head>
<meta charset="utf-8">
<title>Hollwen GmbH – Briefpapier</title>
<link href="https://fonts.googleapis.com/css2?family=Montserrat:wght@400;500&display=swap" rel="stylesheet">
<style>
  :root {
    --ink: #1f1f1f;
    --navy: #131b2c;
    --rule: #a9a9a9;
    --frame: #9a9a9a;
    --icon: #8c8c8c;
    --mark: #a5a5a5;
    --sign: #c9d7ea;
    --paper: #ffffff;
  }
  * { margin: 0; padding: 0; box-sizing: border-box; }
  html, body { width: 849px; height: 1200px; overflow: hidden; background: var(--paper); }
  body { font-family: "Montserrat", sans-serif; color: var(--ink); }
  .letter {
    position: relative; width: 849px; height: 1200px;
    border: 1px solid var(--frame); background: var(--paper);
  }
  .brand {
    position: absolute; left: 346px; top: 38px; width: 157px; height: 57px;
    display: flex; align-items: center; justify-content: center;
    font-size: 24px; font-weight: 400; letter-spacing: 4px; color: var(--navy);
  }
  .rule { position: absolute; left: 100px; width: 670px; height: 0; border-top: 1px solid var(--rule); }
  .rule--top { top: 105px; }
  .rule--bottom { top: 1157px; }
  .tagline {
    position: absolute; left: 100px; width: 670px; top: 116px;
    text-align: center; font-size: 13.5px; letter-spacing: 2.9px; color: var(--ink);
  }
  .sender { position: absolute; left: 105px; top: 208px; font-size: 10.4px; }
  .fold-mark { position: absolute; left: 3px; top: 427px; width: 39px; border-top: 1px solid #c8c8c8; }
  .punch-mark { position: absolute; left: 70px; top: 438px; width: 6px; height: 6px; background: var(--mark); }
  .content { position: absolute; left: 102px; width: 665px; font-size: 15px; line-height: 20px; }
  .salutation { top: 435px; }
  .body-text { top: 475px; }
  .body-text p { text-align: justify; hyphens: auto; margin-bottom: 20px; }
  .closing { top: 734px; }
  .signature {
    position: absolute; left: 109px; top: 760px; width: 263px; height: 36px;
    background: linear-gradient(90deg, var(--sign), #e4ecf6); border-radius: 3px;
  }
  .signer { top: 834px; }
  .footer-item { position: absolute; font-size: 11.5px; line-height: 13px; }
  .footer-item svg { position: absolute; left: -30px; top: -2px; width: 17px; height: 17px; }
</style>
</head>
<body>
<main class="letter">
  <div class="brand">HOLLWEN</div>
  <div class="rule rule--top"></div>
  <div class="tagline">HOLLWEN GMBH PRIVATE INVESTMENT HOLDING</div>

  <div class="sender">HOLLWEN GMBH, Lindauer Weg 52, 80339 München</div>

  <div class="fold-mark"></div>
  <div class="punch-mark"></div>

  <div class="content salutation">Sehr geehrte Damen ubd Herren</div>
  <div class="content body-text">
    <p>dolor sit amet, consetetur sadipscing elitr, sed diam nonumy eirmod tempor invidunt ut labore et dolore magna aliquyam erat, sed diam voluptua. At vero eos et accusam</p>
    <p>nonumy eirmod tempor invidunt ut labore et dolore magna aliquyam erat, sed diam voluptua. sed diam nonumy eirmod tempor invidunt ut labore et dolore magna aliquyam erat, sed diam voluptua. At vero eos et accusam et justo dolor sit amet, consetetur consetetur sadipscing elitr, sed diam nonumy eirmod tempor invidunt ut labore et dolore magna aliquyam erat, sed diam voluptua. At vero eos et accusam et justo dolor sit amet, consetetu At vero eos et accusam et justo dolor sit amet, conseteturdolor sit amet, consetetur sadipscing elitr, sed diam</p>
  </div>

  <div class="content closing">Mit freundlichen Grüßen</div>
  <div class="signature" role="img" aria-label="Handschriftliche Unterschrift von Till Osterwald"></div>
  <div class="content signer">Till Osterwald</div>

  <div class="footer-item" style="left:132px;top:1075px">
    <svg viewBox="0 0 20 20"><circle cx="10" cy="10" r="9" fill="none" stroke="var(--icon)" stroke-width="1.2"/><circle cx="10" cy="8" r="3" fill="var(--icon)"/><path d="M4.5 15.5c1-3 3-4 5.5-4s4.5 1 5.5 4z" fill="var(--icon)"/></svg>
    Dipl.-Wirtschaftsing. (FH)<br>Till Osterwald
  </div>
  <div class="footer-item" style="left:132px;top:1115px">
    <svg viewBox="0 0 20 20"><circle cx="10" cy="10" r="9" fill="none" stroke="var(--icon)" stroke-width="1.2"/><path d="M10 15.5s-3.5-4-3.5-6.5a3.5 3.5 0 0 1 7 0c0 2.5-3.5 6.5-3.5 6.5z" fill="var(--icon)"/><circle cx="10" cy="9" r="1.3" fill="#fff"/></svg>
    Lindauer Weg 52<br>80339 München
  </div>

  <div class="footer-item" style="left:364px;top:1075px">
    <svg viewBox="0 0 20 20"><circle cx="10" cy="10" r="9" fill="none" stroke="var(--icon)" stroke-width="1.2"/><path d="M7 5.5l1.6 2.4-1 1.2c.6 1.3 1.7 2.4 3 3l1.2-1 2.4 1.6-.8 1.8c-4 .2-7.9-3.7-7.7-7.7z" fill="var(--icon)"/></svg>
    089 58210946
  </div>
  <div class="footer-item" style="left:364px;top:1101px">
    <svg viewBox="0 0 20 20"><circle cx="10" cy="10" r="9" fill="none" stroke="var(--icon)" stroke-width="1.2"/><text x="10" y="13.5" text-anchor="middle" font-size="10" font-family="Montserrat, sans-serif" font-weight="500" fill="var(--icon)">@</text></svg>
    info@hollwenbeta.example
  </div>
  <div class="footer-item" style="left:364px;top:1128px">
    <svg viewBox="0 0 20 20"><circle cx="10" cy="10" r="9" fill="none" stroke="var(--icon)" stroke-width="1.2"/><circle cx="10" cy="10" r="5" fill="none" stroke="var(--icon)"/><ellipse cx="10" cy="10" rx="2.2" ry="5" fill="none" stroke="var(--icon)" stroke-width=".8"/><path d="M5 10h10M6 7.5h8M6 12.5h8" stroke="var(--icon)" stroke-width=".8"/></svg>
    hollwenbeta.example
  </div>

  <div class="footer-item" style="left:552px;top:1075px">
    <svg viewBox="0 0 20 20"><circle cx="10" cy="10" r="9" fill="none" stroke="var(--icon)" stroke-width="1.2"/><path d="M10 5v9M6.5 14h7M5 7h10" stroke="var(--icon)" stroke-width="1"/><path d="M4 11l1.5-3.5L7 11zM13 11l1.5-3.5L16 11z" fill="var(--icon)"/></svg>
    Registergericht / Amtsgericht München<br>HRB 527081
  </div>
  <div class="footer-item" style="left:552px;top:1121px">
    <svg viewBox="0 0 20 20"><circle cx="10" cy="10" r="9" fill="none" stroke="var(--icon)" stroke-width="1.2"/><path d="M5 8l5-3 5 3z" fill="var(--icon)"/><path d="M6.5 9v4M9 9v4M11 9v4M13.5 9v4" stroke="var(--icon)" stroke-width="1.1"/><path d="M5 14h10" stroke="var(--icon)" stroke-width="1.2"/></svg>
    IBAN DE918204 5571 0009 1826 40
  </div>

  <div class="rule rule--bottom"></div>
</main>
</body>
</html>
```